Postcard Design

We are a full service lawn maintenace and landscapig company. Everything from maintenance, fertilizer programs, to design and install.
I would like the card to have a classy look including our logo which is attached. The logo would just have to contain the lettering and the swooshes not the pine tree background if not needed.

Industry/Entity Type

It Company

```html
<!DOCTYPE html>
<html lang="en">
<head>
<meta charset="utf-8">
<title>Tall Cedar Landscaping – Postcard</title>
<link href="https://fonts.googleapis.com/css2?family=Ubuntu:wght@400;500;700&display=swap" rel="stylesheet">
<style>
  :root {
    --bg: #e9e9e7;
    --forest: #1d4a22;
    --forest-text: #1f4d24;
    --white: #ffffff;
    --cream: #f6ecd6;
    --brown-text: #6b4a2a;
    --list-text: #5b4630;
    --badge: #ef7c63;
    --square: #8a9bb8;
    --lawn: #3f7a2a;
    --sky: #9cc3e6;
  }
  * { margin: 0; padding: 0; box-sizing: border-box; }
  html, body { width: 954px; height: 1200px; overflow: hidden; }
  body { background: var(--bg); font-family: "Ubuntu", sans-serif; position: relative; }

  .card { position: absolute; width: 747px; height: 536px; background: var(--white); overflow: hidden;
          box-shadow: 0 4px 14px rgba(0,0,0,.25); }
  .card--front { left: 54px; top: 41px; }
  .card--back { left: 110px; top: 608px; }

  .hero-photo { position: absolute; left: 0; top: 0; width: 747px; height: 487px;
    background: linear-gradient(180deg, var(--sky) 0%, #b9cfd8 22%, #c9b08a 38%, #9d8a66 52%, #3c6a2a 62%, var(--lawn) 100%); }

  .social-square { position: absolute; width: 38px; height: 38px; border-radius: 5px; background: var(--square); }
  .card--front .social-square { left: 654px; top: 38px; width: 58px; height: 58px; border-radius: 6px; }
  .card--back .social-square { left: 672px; top: 40px; }

  .brand-name { position: absolute; left: 0; width: 100%; text-align: center; font-weight: 700;
    text-transform: uppercase; line-height: 0.92; letter-spacing: 1px; }
  .card--front .brand-name { top: 345px; left: 150px; width: 450px; color: var(--white); font-size: 40px; }
  .card--back .brand-name { top: 40px; left: 190px; width: 360px; color: var(--forest-text); font-size: 34px; }

  .footer-band { position: absolute; left: 0; bottom: 0; width: 100%; height: 44px; background: var(--forest);
    color: var(--white); display: flex; align-items: center; padding: 0 30px; font-size: 14px; }
  .card--front .footer-band { border-top: 3px solid var(--white); height: 47px; }
  .footer-band .address { flex: 1; }
  .footer-band .cta { margin-right: 14px; font-size: 14px; }
  .footer-band .phone { display: flex; align-items: center; gap: 6px; font-size: 20px; font-weight: 700; }

  .tagline { position: absolute; left: 30px; top: 138px; display: flex; align-items: center; gap: 16px;
    color: var(--brown-text); font-size: 15px; font-weight: 700; }
  .services-top { position: absolute; left: 78px; top: 172px; display: grid; grid-template-columns: 198px 200px;
    row-gap: 4px; list-style: none; color: var(--list-text); font-size: 16px; }
  .services-top li::before, .services-bottom li::before { content: "» "; color: #9a7a4c; }

  .badge { position: absolute; left: 551px; top: 132px; width: 112px; height: 112px; border-radius: 50%;
    background: var(--badge); display: flex; align-items: center; justify-content: center; }
  .badge-inner { width: 92px; height: 92px; border-radius: 50%; background: var(--white); border: 2px solid var(--badge);
    display: flex; flex-direction: column; align-items: center; justify-content: center; color: var(--badge);
    transform: rotate(-12deg); }
  .badge-inner .big { font-size: 26px; font-weight: 700; line-height: 1; }
  .badge-inner .small { font-size: 15px; font-weight: 500; letter-spacing: 1px; }

  .photo-row { position: absolute; left: 0; top: 232px; width: 100%; height: 180px; display: flex; gap: 2px; }
  .photo { height: 100%; }
  .photo--mower { width: 274px; background: linear-gradient(180deg, #8fb3cf 0%, #5f8f4a 35%, #4f8a2e 100%); }
  .photo--lawn { width: 235px; background: linear-gradient(180deg, #a86b45 0%, #6f8a4a 22%, #3f7d24 55%, #5ea03a 100%); }
  .photo--truck { width: 234px; background: linear-gradient(180deg, #8fb9dc 0%, #7f9a6a 35%, #b8bcbc 70%, #d0d0cc 100%); }

  .services-band { position: absolute; left: 0; top: 412px; width: 100%; height: 80px; background: var(--cream); }
  .services-bottom { position: absolute; left: 38px; top: 22px; display: grid; grid-template-columns: 375px 320px;
    row-gap: 4px; list-style: none; color: var(--list-text); font-size: 14px; }
</style>
</head>
<body>

<section class="card card--front">
  <div class="hero-photo" role="img" aria-label="Photo of a stone manor house with manicured lawn, topiary trees and hedges"></div>
  <div class="social-square" aria-hidden="true"></div>
  <div class="brand-name">Tall Cedar<br>Landscaping</div>
  <div class="footer-band">
    <span class="address">18210 Birch Lane Fairview, MI 48000</span>
    <span class="cta">Call Now for FREE ESTIMATE</span>
    <span class="phone">
      <svg width="20" height="20" viewBox="0 0 24 24" aria-hidden="true"><circle cx="12" cy="12" r="10.5" fill="none" stroke="#fff" stroke-width="1.8"/><path d="M8.5 6.8c.5-.4 1.1-.3 1.4.2l1 1.7c.3.5.1 1-.3 1.3l-.7.5c.6 1.4 1.6 2.5 3 3.1l.5-.7c.3-.4.9-.6 1.3-.3l1.7 1c.5.3.6.9.2 1.4l-.8.9c-.6.6-1.5.8-2.3.4-2.7-1.2-4.8-3.3-6-6-.4-.8-.2-1.7.4-2.3z" fill="#fff"/></svg>
      555 014 2287
    </span>
  </div>
</section>

<section class="card card--back">
  <div class="brand-name">Tall Cedar<br>Landscaping</div>
  <div class="social-square" aria-hidden="true"></div>

  <p class="tagline">
    <svg width="22" height="22" viewBox="0 0 22 22" aria-hidden="true"><circle cx="11" cy="11" r="11" fill="#5b4630"/><path d="M8 6l8 5-8 5z" fill="#fff"/></svg>
    We are a full service lawn maintenace and landscapig company.
  </p>
  <ul class="services-top">
    <li>Lavn Maintenance</li>
    <li>Design Landscaping</li>
    <li>Fertilizer Programs</li>
    <li>Install</li>
  </ul>

  <div class="badge">
    <div class="badge-inner"><span class="big">BEST</span><span class="small">PRICE</span></div>
  </div>

  <div class="photo-row">
    <div class="photo photo--mower" role="img" aria-label="Photo of a worker on a red riding mower cutting grass"></div>
    <div class="photo photo--lawn" role="img" aria-label="Photo of a freshly striped green lawn in front of houses"></div>
    <div class="photo photo--truck" role="img" aria-label="Photo of a red company pickup truck with a trailer on a street"></div>
  </div>

  <div class="services-band">
    <ul class="services-bottom">
      <li>Residential and Commercial Lawn Maintenance</li>
      <li>Sprinkler Service and Installation</li>
      <li>Landscape Installation</li>
      <li>Residential and Commercial Snow Removal</li>
    </ul>
  </div>

  <div class="footer-band">
    <span class="address">18210 Birch Lane Fairview, MI 48000</span>
    <span class="cta">Call Now for FREE ESTIMATE</span>
    <span class="phone">
      <svg width="20" height="20" viewBox="0 0 24 24" aria-hidden="true"><circle cx="12" cy="12" r="10.5" fill="none" stroke="#fff" stroke-width="1.8"/><path d="M8.5 6.8c.5-.4 1.1-.3 1.4.2l1 1.7c.3.5.1 1-.3 1.3l-.7.5c.6 1.4 1.6 2.5 3 3.1l.5-.7c.3-.4.9-.6 1.3-.3l1.7 1c.5.3.6.9.2 1.4l-.8.9c-.6.6-1.5.8-2.3.4-2.7-1.2-4.8-3.3-6-6-.4-.8-.2-1.7.4-2.3z" fill="#fff"/></svg>
      555 014 2287
    </span>
  </div>
</section>

</body>
</html>
```